Create for us a Shop-Stopper Business Card

We need a standout, first class business card to go along with our new brand strategy. Sleek, Contemporary and fresh.

Colors and theme must sync with our websitewww.pelvorpower.co.uk

We want a business card that has a global brand appeal. TKR Energy is a small UK renewable company that specialises in energy projects in Africa. We want a business card that has the following characteristics: Very short, precise, global, stand out, NOT TOO LOUD but contemporary. The company's colour themes are White, Grey with a hint of green.

Target Market(s)

Business exec, high net worth individuals, investors, commercial leaders, suppliers, government officials

Industry/Entity Type

Solar Energy

Contact Information for Business Card

Logo, Name, Title, Address, web address, email,

Requirements
Must have
• Logo must be sharp
Nice to have
• Adapt fonts from the logo. The large circular side of the logo at the back in a very refreshing way
Should not have
• No solar panel shapes or image.Very little black. If possible avoid black. Its not coming out nice. I think !!!

```html
<!DOCTYPE html>
<html lang="en">
<head>
<meta charset="utf-8">
<title>TKR Energy – Business Card</title>
<link href="https://fonts.googleapis.com/css2?family=Questrial&display=swap" rel="stylesheet">
<style>
  :root {
    --backdrop: #e6e6e3;
    --card-white: #ffffff;
    --card-charcoal: #333333;
    --band-grey: #3a3a3a;
    --brand-green: #0f7a3c;
    --leaf-green: #3fae49;
    --faint-green: #e9f2ed;
    --text-grey: #555555;
    --title-dark: #333333;
    --accent-red: #d5202e;
    --white: #ffffff;
  }
  * { margin: 0; padding: 0; box-sizing: border-box; }
  html, body { width: 1200px; height: 987px; overflow: hidden; }
  body {
    background: var(--backdrop);
    font-family: "Questrial", "Century Gothic", sans-serif;
    position: relative;
  }
  .card {
    position: absolute;
    left: 293px;
    width: 615px;
    height: 351px;
    overflow: hidden;
    box-shadow: 0 3px 8px rgba(0,0,0,0.25);
  }
  .card-front { top: 130px; background: var(--card-white); }
  .card-back { top: 505px; background: var(--card-charcoal); }

  .front-decoration {
    position: absolute;
    left: 351px; top: -1px;
    width: 352px; height: 352px;
    border-radius: 50%;
    background: var(--faint-green);
  }
  .logo-band {
    position: absolute;
    left: 0; top: 37px;
    width: 59px; height: 73px;
    background: var(--band-grey);
  }
  .logo-dot {
    position: absolute;
    left: 31px; top: 38px;
    width: 72px; height: 72px;
    border-radius: 50%;
    background: var(--brand-green);
    border: 4px solid var(--card-white);
  }
  .brand-name {
    position: absolute;
    left: 111px; top: 46px;
    font-size: 40px;
    line-height: 48px;
    color: var(--text-grey);
    letter-spacing: 0.5px;
    white-space: nowrap;
  }
  .brand-rule {
    position: absolute;
    left: 111px; top: 95px;
    width: 279px; height: 2px;
    background: var(--accent-red);
  }
  .holder-name {
    position: absolute;
    left: 111px; top: 130px;
    font-size: 22px;
    color: var(--brand-green);
    letter-spacing: 0.5px;
  }
  .holder-name strong { font-weight: 700; }
  .holder-title {
    position: absolute;
    left: 111px; top: 159px;
    font-size: 16px;
    color: var(--title-dark);
    letter-spacing: 0.3px;
  }
  .holder-title strong { font-weight: 700; }
  .address {
    position: absolute;
    left: 111px; top: 193px;
    font-size: 16px;
    line-height: 22px;
    color: var(--text-grey);
    font-style: normal;
  }
  .contact-list {
    position: absolute;
    left: 111px; top: 248px;
    list-style: none;
    font-size: 16px;
    line-height: 24.5px;
    color: var(--text-grey);
  }
  .contact-list li { display: flex; align-items: center; gap: 7px; }
  .contact-icon { width: 14px; height: 14px; flex: none; }

  .back-decoration {
    position: absolute;
    left: -148px; top: 75px;
    width: 296px; height: 296px;
    border-radius: 50%;
    background: var(--brand-green);
  }
  .back-brand {
    position: absolute;
    left: 272px; top: 152px;
    color: var(--white);
  }
  .back-brand-name {
    font-size: 36px;
    line-height: 40px;
    letter-spacing: 0.5px;
    white-space: nowrap;
  }
  .back-brand-rule {
    width: 241px; height: 2px;
    background: var(--white);
    margin: 2px 0 6px;
  }
  .back-web {
    font-size: 15px;
    letter-spacing: 1.6px;
    text-transform: uppercase;
  }
</style>
</head>
<body>

<section class="card card-front" aria-label="Business card front">
  <div class="front-decoration"></div>
  <div class="logo-band"></div>
  <div class="logo-dot"></div>
  <div class="brand-name">TKR ENERGY</div>
  <div class="brand-rule"></div>

  <h1 class="holder-name"><strong>DANIEL</strong> HARTLEY</h1>
  <p class="holder-title"><strong>CEO</strong>/FOUNDER</p>

  <address class="address">
    214 Fernbrook Road<br>
    Leeds, West Yorkshire LS6 2QT
  </address>

  <ul class="contact-list">
    <li>
      <svg class="contact-icon" viewBox="0 0 14 14" aria-hidden="true">
        <path d="M3 1 L5.2 3.6 L4 5.2 Q5.5 8.3 8.8 10 L10.4 8.8 L13 11 L11.4 13 Q5.5 12.5 1 2.6 Z" fill="#0f7a3c"/>
      </svg>
      0113 496 0871
    </li>
    <li>
      <svg class="contact-icon" viewBox="0 0 14 14" aria-hidden="true">
        <rect x="1" y="3" width="12" height="8.5" fill="#0f7a3c"/>
        <path d="M1.5 3.5 L7 8 L12.5 3.5" fill="none" stroke="#ffffff" stroke-width="1.2"/>
      </svg>
      name@pelvorpower.co.uk
    </li>
    <li>
      <svg class="contact-icon" viewBox="0 0 14 14" aria-hidden="true">
        <circle cx="7" cy="7" r="6" fill="#0f7a3c"/>
        <ellipse cx="7" cy="7" rx="2.6" ry="6" fill="none" stroke="#ffffff" stroke-width="0.9"/>
        <line x1="1" y1="7" x2="13" y2="7" stroke="#ffffff" stroke-width="0.9"/>
      </svg>
      www.pelvorpower.co.uk
    </li>
  </ul>
</section>

<section class="card card-back" aria-label="Business card back">
  <div class="back-decoration"></div>
  <div class="back-brand">
    <div class="back-brand-name">TKR ENERGY</div>
    <div class="back-brand-rule"></div>
    <div class="back-web">www.pelvorpower.co.uk</div>
  </div>
</section>

</body>
</html>
```